Need wine label for brand that is named: Casmerel Vineyards & Winery

Casmerel is a yoga way of breathing. In Sanskrit Casmerel means "flying up." I would like a creative wine label that articulates Casmerel. The label should include a graphic and the name Casmerel on one line and Vineyards & Winery in smaller print underneath Casmerel.

```html
<!DOCTYPE html>
<html lang="en">
<head>
<meta charset="utf-8">
<title>Casmerel Vineyards &amp; Winery – Wine Label</title>
<link rel="stylesheet" href="https://fonts.googleapis.com/css2?family=Montserrat:wght@300&family=Pacifico&display=swap">
<style>
  :root {
    --stage: #ffffff;
    --purple: #5e3399;
    --purple-light: #8a62bd;
    --purple-mist: #a586cf;
    --band-dark: rgba(20, 6, 40, 0.75);
    --ink: #ffffff;
    --shadow: #111111;
  }
  * { margin: 0; padding: 0; box-sizing: border-box; }
  html, body {
    width: 1200px;
    height: 678px;
    overflow: hidden;
    background: var(--stage);
  }
  .canvas {
    position: relative;
    width: 1200px;
    height: 678px;
  }
  .label {
    position: absolute;
    left: 365px;
    top: 70px;
    width: 470px;
    height: 538px;
    overflow: hidden;
    background:
      radial-gradient(ellipse 120px 90px at 40px 120px, var(--purple-mist) 0%, transparent 80%),
      radial-gradient(ellipse 110px 140px at 30px 420px, var(--purple-mist) 0%, transparent 80%),
      radial-gradient(ellipse 90px 80px at 110px 500px, var(--purple-light) 0%, transparent 85%),
      linear-gradient(90deg, var(--purple-light) 0%, var(--purple) 45%, var(--purple) 100%);
    box-shadow: 0 2px 6px rgba(0, 0, 0, 0.25);
  }
  .label__band {
    position: absolute;
    left: 138px;
    top: 0;
    width: 72px;
    height: 100%;
    background: linear-gradient(180deg, var(--band-dark) 0%, rgba(20, 6, 40, 0.35) 45%, rgba(255, 255, 255, 0.08) 100%);
  }
  .brand-name,
  .brand-tagline {
    position: absolute;
    writing-mode: vertical-rl;
    transform: rotate(180deg);
    color: var(--ink);
    white-space: nowrap;
  }
  .brand-name {
    left: 18px;
    top: 20px;
    height: 505px;
    font-family: "Pacifico", cursive;
    font-size: 92px;
    line-height: 1;
    text-shadow: -5px 5px 0 var(--shadow);
  }
  .brand-tagline {
    left: 158px;
    top: 40px;
    height: 490px;
    font-family: "Montserrat", sans-serif;
    font-weight: 300;
    font-size: 31px;
    letter-spacing: 3px;
    line-height: 1;
  }
  .label__art {
    position: absolute;
    left: 235px;
    top: 95px;
    width: 222px;
    height: 443px;
  }
</style>
</head>
<body>
  <main class="canvas">
    <section class="label">
      <div class="label__band"></div>
      <h1 class="brand-name">Casmerel</h1>
      <p class="brand-tagline">Vineyards &amp; Winery</p>
      <svg class="label__art" role="img" aria-label="White illustration of a wine glass with wine splashing upward out of it, with a bunch of grapes at its base" viewBox="0 0 222 443">
        <defs>
          <radialGradient id="art-glow" cx="50%" cy="45%" r="60%">
            <stop offset="0%" stop-color="#ffffff" stop-opacity="0.55"/>
            <stop offset="100%" stop-color="#ffffff" stop-opacity="0.12"/>
          </radialGradient>
        </defs>
        <rect width="222" height="443" rx="18" fill="url(#art-glow)"/>
      </svg>
    </section>
  </main>
</body>
</html>
```